Logo/Business Card design for a Chef using Tattoo Inspiration- Design must meet business card requirements on Pellu's website - link below

Business Card/Logo Design for my little brother- I would like to design and order my brother business cards for his business. He has a passion for cooking and was recently promoted to head chef. I have a picture of his tattoo that I would like re-imagined so it can be incorporate in the design of the business card or used to create a logo.
Must haves
1. Tattoo incorporated into the design
2. card Details below
must be able to use design to create the business card on Pellu.
Card details:
Business Name: Spoon And Ember
Name: Dennis Holloway
Title: Private Chef
Phone: 408-555-0172
Instragram: spoon_and_ember

optional use: via text or pictures incorporated in card design.
specialized in Korean, Italian, Peruvian, American, Chinese.
Private Chef
Dinner Parties
Special Occasions

type of card Square with round edges: the picture of his tattoo incorporated within the design.
Square Business Card templates to download https://help.pellu-example.com/hc/en-us/articles/500000001-Square-Business-Card-templates-to-download
Create business card here using their requirements.
https://www.pellu-example.com/us/design-templates/business-cards/?finishingOption=square_corners&laminate=mattelam&origPaperType=classic&paperType=classic&productType=businesscard_us
Card details

```html
<!DOCTYPE html>
<html lang="en">
<head>
<meta charset="utf-8">
<title>Spoon And Ember – Square Business Card</title>
<link href="https://fonts.googleapis.com/css2?family=Montserrat:wght@400;500;800&family=Playfair+Display:wght@400&display=swap" rel="stylesheet">
<style>
  :root {
    --page-bg: #ffffff;
    --card-black: #0d0d0d;
    --frame-white: #f4f4f4;
    --chef-red: #c52b23;
    --text-white: #ffffff;
    --muted-white: #d9d9d9;
  }
  html, body {
    margin: 0;
    padding: 0;
    width: 914px;
    height: 1200px;
    overflow: hidden;
    background: var(--page-bg);
  }
  .canvas {
    position: relative;
    width: 914px;
    height: 1200px;
  }
  .card {
    position: absolute;
    top: 425px;
    width: 350px;
    height: 350px;
  }
  .card--front { left: 76px; }
  .card--back { left: 484px; }
  .card-surface { fill: var(--card-black); }
  .frame-line { stroke: var(--frame-white); stroke-width: 1.4; fill: none; }
  .banner { fill: var(--chef-red); }
  .banner-edge { fill: none; stroke: var(--text-white); stroke-width: 2; }
  .brand-name {
    font-family: 'Montserrat', sans-serif;
    font-weight: 800;
    fill: var(--text-white);
    text-anchor: middle;
    letter-spacing: 0.5px;
  }
  .person-name {
    font-family: 'Playfair Display', serif;
    font-size: 24px;
    fill: var(--text-white);
    text-anchor: middle;
  }
  .person-title {
    font-family: 'Montserrat', sans-serif;
    font-weight: 500;
    font-size: 15px;
    letter-spacing: 1.6px;
    fill: var(--chef-red);
    text-anchor: middle;
  }
  .title-rule { stroke: var(--muted-white); stroke-width: 1; }
  .contact-text {
    font-family: 'Montserrat', sans-serif;
    font-weight: 400;
    font-size: 7.5px;
    fill: var(--muted-white);
  }
  .contact-badge { fill: var(--chef-red); }
  .phone-icon { fill: var(--text-white); }
</style>
</head>
<body>
<main class="canvas">

  <svg class="card card--front" viewBox="0 0 344 344" aria-label="Business card front">
    <rect class="card-surface" x="0" y="0" width="344" height="344"/>

    <!-- frame -->
    <path class="frame-line" d="M72 25 H25 V320 H62"/>
    <path class="frame-line" d="M272 25 H318 V320 H290"/>
    <line class="frame-line" x1="150" y1="320" x2="186" y2="320"/>

    <!-- banner -->
    <polygon class="banner" points="85,0 261,0 261,140 173,177 85,140"/>
    <polyline class="banner-edge" points="85,0 85,140 173,177 261,140 261,0"/>
    <text class="brand-name" x="173" y="82" font-size="21">SPOON AND</text>
    <text class="brand-name" x="173" y="112" font-size="21">EMBER</text>

    <!-- name & title -->
    <text class="person-name" x="172" y="220">Dennis Holloway</text>
    <text class="person-title" x="172" y="247">Private Chef</text>
    <line class="title-rule" x1="99" y1="254" x2="245" y2="254"/>

    <!-- contacts -->
    <circle class="contact-badge" cx="78" cy="320" r="7"/>
    <path class="phone-icon" d="M75.2 316.2 l1.6 -0.6 l1.2 2.2 l-1 0.9 q0.8 1.8 2.4 2.6 l0.9 -1 l2.2 1.2 l-0.6 1.6 q-3.4 0.4 -5.8 -2.2 q-1.6 -2 -0.9 -4.7z"/>
    <text class="contact-text" x="90" y="322.6">408-555-0172</text>

    <circle class="contact-badge" cx="199" cy="320" r="7"/>
    <text class="contact-text" x="211" y="322.6">spoon_and_ember</text>
  </svg>

  <svg class="card card--back" viewBox="0 0 344 344" aria-label="Business card back">
    <rect class="card-surface" x="0" y="0" width="344" height="344"/>
    <rect class="frame-line" x="26" y="25" width="292" height="294"/>
    <text class="brand-name" x="172" y="170" font-size="30">SPOON AND</text>
    <text class="brand-name" x="172" y="208" font-size="30">EMBER</text>
  </svg>

</main>
</body>
</html>
```